Business Cards and Stationery
Vellomar Development Company
I need single sided standard sized Business Card [3.5" x 2"]
Not sure. Use something compatible with logo.
Professional
Xxxx Xxxxxxx
President
12345 Xxxxxxxxx Xxxxx
Xxxxxxxxx, Xxxxxxxxxx 12345
xxxxxxxxxxx@xxxxxxxxx.xxx
Contractor's License No. 123456
Not that the information will serve as placeholders until the project is awarded and finalized. Actual information will be provided to create final source files.

```html
<!DOCTYPE html>
<html lang="en">
<head>
<meta charset="utf-8">
<title>Vellomar Development Company – Stationery</title>
<link href="https://fonts.googleapis.com/css2?family=Montserrat:wght@800&family=Open+Sans:wght@400;600&display=swap" rel="stylesheet">
<style>
  :root{
    --navy:#24286e;
    --navy-deep:#161a52;
    --grey:#c9cbd1;
    --grey-light:#e6e7ea;
    --paper:#ffffff;
    --ink:#3a3a46;
    --backdrop:#eceae6;
  }
  *{box-sizing:border-box;margin:0;padding:0}
  html,body{width:1200px;height:504px;overflow:hidden;background:var(--backdrop)}
  body{position:relative;font-family:"Open Sans",Arial,sans-serif;color:var(--ink)}
  .sheet{position:absolute;background:var(--paper);overflow:hidden;box-shadow:0 2px 6px rgba(0,0,0,.18)}
  .wave{position:absolute;left:0;bottom:0;width:100%}
  .brand{display:flex;flex-direction:column;align-items:center;gap:3px}
  .brand-dot{width:18px;height:18px;border-radius:50%;background:var(--navy)}
  .brand-name{font-family:"Montserrat",Arial,sans-serif;font-weight:800;color:var(--navy);letter-spacing:.5px;font-size:13px;line-height:1}
  .brand.row{flex-direction:row;gap:5px}
  .brand.row .brand-dot{width:12px;height:12px}
  .brand.row .brand-name{font-size:10px}
  .brand.light .brand-dot{background:var(--paper)}
  .brand.light .brand-name{color:var(--paper)}
  .faint-disc{position:absolute;border-radius:50%;background:var(--grey-light)}
  .footer-text{position:absolute;font-size:4.5px;line-height:1.4;color:var(--paper)}

  /* business cards */
  .card-front{left:24px;top:108px;width:144px;height:72px}
  .card-front .brand{position:absolute;left:10px;top:26px}
  .card-front .brand-dot{width:12px;height:12px}
  .card-front .brand-name{font-size:8px}
  .card-contact{position:absolute;right:8px;top:7px;font-size:3.6px;line-height:1.45;text-align:left;width:54px}
  .card-contact .name{font-weight:600;color:var(--navy)}
  .card-back{left:24px;top:197px;width:144px;height:80px;background:linear-gradient(180deg,var(--navy) 0%,var(--navy-deep) 100%)}
  .card-back .brand{position:absolute;left:50%;top:50%;transform:translate(-50%,-50%)}
  .card-plain{left:24px;top:293px;width:144px;height:72px}
  .card-plain .brand{position:absolute;left:50%;top:50%;transform:translate(-50%,-50%)}
  .card-plain .brand-dot{width:14px;height:14px}
  .card-plain .brand-name{font-size:8px}

  /* letterheads */
  .letterhead{top:43px;width:305px;height:413px}
  .letterhead.fax{left:187px}
  .letterhead.blank{left:509px}
  .letterhead .brand{position:absolute;left:50%;top:14px;transform:translateX(-50%)}
  .letterhead .faint-disc{right:20px;bottom:50px;width:78px;height:78px}
  .letterhead .footer-text{left:16px;bottom:8px}
  .fax-title{position:absolute;left:16px;top:62px;font-family:"Montserrat",Arial,sans-serif;font-weight:800;font-size:10px;color:var(--ink)}
  .fax-table{position:absolute;left:16px;top:78px;width:198px;border-collapse:collapse;font-size:4px}
  .fax-table td{border:0.6px solid #9a9aa5;height:7px;padding:0 2px;width:50%}
  .fax-options{position:absolute;left:16px;top:122px;width:198px;display:flex;justify-content:space-between;font-size:4px}
  .fax-options span::before{content:"";display:inline-block;width:3px;height:3px;border:0.5px solid var(--ink);margin-right:1.5px;vertical-align:middle}

  /* envelopes */
  .envelope{left:840px;width:336px}
  .envelope.back{top:43px;height:137px}
  .envelope.back .brand{position:absolute;left:50%;top:10px;transform:translateX(-50%)}
  .envelope.back .brand-dot{width:14px;height:14px}
  .envelope.front{height:103px}
  .envelope.front.one{top:216px}
  .envelope.front.two{top:343px}
  .envelope.front .brand{position:absolute;left:16px;top:12px}
  .envelope.front .faint-disc{right:18px;top:18px;width:56px;height:56px}
  .envelope.front .sender{position:absolute;left:16px;top:30px;font-size:3.8px;line-height:1.4}
</style>
</head>
<body>

<svg width="0" height="0" style="position:absolute" aria-hidden="true">
  <defs>
    <symbol id="wave-band" viewBox="0 0 300 60" preserveAspectRatio="none">
      <path d="M0 18 C70 2 150 2 210 18 S280 34 300 20 L300 60 L0 60Z" fill="#c9cbd1"/>
      <path d="M0 30 C70 14 150 16 210 30 S280 44 300 30 L300 60 L0 60Z" fill="#24286e"/>
    </symbol>
  </defs>
</svg>

<!-- business card, front -->
<section class="sheet card-front">
  <div class="brand row"><span class="brand-dot"></span><span class="brand-name">VELLOMAR</span></div>
  <div class="card-contact">
    <div class="name">Xxxx Xxxxxxx</div>
    <div>President</div>
    <div>12345 Xxxxxxxxx Xxxxx</div>
    <div>Xxxxxxxxx, Xxxxxxxxxx 12345</div>
    <div>xxxxxxxxxxx@xxxxxxxxx.xxx</div>
  </div>
  <svg class="wave" height="20"><use href="#wave-band"/></svg>
</section>

<!-- business card, back -->
<section class="sheet card-back">
  <div class="brand light"><span class="brand-dot"></span><span class="brand-name">VELLOMAR</span></div>
</section>

<!-- business card, plain -->
<section class="sheet card-plain">
  <div class="brand"><span class="brand-dot"></span><span class="brand-name">VELLOMAR</span></div>
</section>

<!-- fax letterhead -->
<section class="sheet letterhead fax">
  <div class="brand"><span class="brand-dot"></span><span class="brand-name">VELLOMAR</span></div>
  <div class="fax-title">FAX:</div>
  <table class="fax-table">
    <tr><td>To:</td><td>From:</td></tr>
    <tr><td>Fax:</td><td>Pages:</td></tr>
    <tr><td>Phone:</td><td>Date:</td></tr>
    <tr><td>Re:</td><td>CC:</td></tr>
    <tr><td colspan="2">Number of Pages:</td></tr>
  </table>
  <div class="fax-options">
    <span>Urgent</span><span>For Review</span><span>Please Comment</span><span>Please Reply</span>
  </div>
  <div class="faint-disc"></div>
  <svg class="wave" height="44"><use href="#wave-band"/></svg>
  <div class="footer-text">12345 Xxxxxxxxx Xxxxx<br>Xxxxxxxxx, Xxxxxxxxxx 12345</div>
</section>

<!-- letterhead -->
<section class="sheet letterhead blank">
  <div class="brand"><span class="brand-dot"></span><span class="brand-name">VELLOMAR</span></div>
  <div class="faint-disc"></div>
  <svg class="wave" height="44"><use href="#wave-band"/></svg>
  <div class="footer-text">12345 Xxxxxxxxx Xxxxx<br>Xxxxxxxxx, Xxxxxxxxxx 12345</div>
</section>

<!-- envelope, back -->
<section class="sheet envelope back">
  <svg width="336" height="137" viewBox="0 0 336 137" style="position:absolute;left:0;top:0">
    <polygon points="0,0 336,0 168,70" fill="#24286e"/>
    <polygon points="0,0 336,0 168,58" fill="#161a52"/>
    <polygon points="0,0 168,70 0,8" fill="#c9cbd1"/>
    <polygon points="336,0 168,70 336,8" fill="#c9cbd1"/>
  </svg>
  <div class="brand light"><span class="brand-dot"></span><span class="brand-name">VELLOMAR</span></div>
</section>

<!-- envelope, front -->
<section class="sheet envelope front one">
  <div class="brand row"><span class="brand-dot"></span><span class="brand-name">VELLOMAR</span></div>
  <div class="sender">12345 Xxxxxxxxx Xxxxx<br>Xxxxxxxxx, Xxxxxxxxxx 12345</div>
  <div class="faint-disc"></div>
  <svg class="wave" height="26"><use href="#wave-band"/></svg>
</section>

<!-- envelope, front variant -->
<section class="sheet envelope front two">
  <div class="brand row"><span class="brand-dot"></span><span class="brand-name">VELLOMAR</span></div>
  <div class="sender">12345 Xxxxxxxxx Xxxxx<br>Xxxxxxxxx, Xxxxxxxxxx 12345</div>
  <div class="faint-disc"></div>
  <svg class="wave" height="30"><use href="#wave-band"/></svg>
</section>

</body>
</html>
```